Tarrow Creek plumbing plumbing company business card design

Something sinilar to business card i upload it is my old business card design
And have a good watermark with the logo or majority of the logot in rhe background as watermark

Plumbing business similar to uploaded design with a nice watermark of the logo

Font styles to use
Script

Colors

Designer to choose colors to be used in the design.

```html
<!DOCTYPE html>
<html lang="en">
<head>
<meta charset="utf-8">
<title>Tarrow Creek Plumbing – Business Card</title>
<link rel="stylesheet" href="https://fonts.googleapis.com/css2?family=Open+Sans:wght@400;600;700;800&display=swap">
<style>
  :root {
    --backdrop: #3a3a3c;
    --card-black: #0c0c0e;
    --card-black-band: #1c1b21;
    --card-blue: #0a7fd0;
    --card-blue-deep: #0670bb;
    --brand-blue: #1e8fe0;
    --ink: #0b0b0d;
    --white: #ffffff;
    --watermark-dark: rgba(255,255,255,0.06);
    --watermark-blue: rgba(0,40,90,0.18);
  }
  * { box-sizing: border-box; margin: 0; padding: 0; }
  html, body { width: 1200px; height: 900px; overflow: hidden; }
  body {
    background: var(--backdrop);
    font-family: "Open Sans", Arial, sans-serif;
    position: relative;
  }
  .card {
    position: absolute;
    left: 250px;
    width: 700px;
    height: 400px;
    overflow: hidden;
    box-shadow: 0 10px 26px rgba(0,0,0,0.45);
  }

  /* Front card */
  .card--front {
    top: 40px;
    background: linear-gradient(160deg, #141416 0%, var(--card-black) 70%);
  }
  .card--front .watermark {
    position: absolute;
    left: -90px; top: 30px;
    width: 330px; height: 330px;
    border-radius: 50%;
    background: var(--watermark-dark);
  }
  .card--front .footer-band {
    position: absolute;
    left: 0; right: 0; bottom: 0;
    height: 86px;
    background: var(--card-black-band);
    display: flex;
    align-items: flex-start;
    justify-content: center;
    padding-top: 8px;
  }
  .website-front {
    color: var(--white);
    font-size: 16px;
    font-weight: 600;
    letter-spacing: 0.3px;
  }
  .brand {
    position: absolute;
    display: flex;
    align-items: center;
    gap: 14px;
  }
  .brand__mark {
    width: 22px; height: 22px;
    flex: none;
  }
  .brand__name {
    font-weight: 800;
    text-transform: uppercase;
    line-height: 1.05;
    letter-spacing: 2px;
  }
  .card--front .brand { right: 70px; top: 130px; }
  .card--front .brand__mark { background: var(--brand-blue); }
  .card--front .brand__name { color: var(--white); font-size: 34px; }

  /* Back card */
  .card--back {
    top: 470px;
    background: linear-gradient(165deg, var(--card-blue) 0%, var(--card-blue-deep) 100%);
  }
  .card--back .watermark {
    position: absolute;
    left: -60px; top: 20px;
    width: 380px; height: 380px;
    border-radius: 50%;
    background: var(--watermark-blue);
  }
  .card--back .contact-panel {
    position: absolute;
    left: 0; top: 255px;
    width: 300px; height: 145px;
    background: rgba(0,50,110,0.14);
  }
  .card--back .brand { right: 50px; top: 40px; }
  .card--back .brand__mark { background: var(--white); }
  .card--back .brand__name { color: var(--ink); font-size: 30px; }

  .person {
    position: absolute;
    left: 44px; top: 182px;
  }
  .person__name {
    color: var(--ink);
    font-size: 27px;
    font-weight: 800;
    letter-spacing: 0.5px;
  }
  .person__title {
    color: var(--white);
    font-size: 21px;
    font-weight: 400;
    margin-top: -4px;
  }
  .divider {
    position: absolute;
    left: 44px; right: 70px; top: 262px;
    height: 1.5px;
    background: var(--ink);
  }
  .contact-list {
    position: absolute;
    left: 40px; top: 282px;
    list-style: none;
  }
  .contact-list li {
    display: flex;
    align-items: center;
    gap: 14px;
    color: var(--white);
    font-size: 19px;
    height: 30px;
  }
  .contact-list svg { width: 18px; height: 18px; fill: var(--ink); flex: none; }
  .address {
    position: absolute;
    right: 70px; bottom: 34px;
    text-align: right;
    color: var(--white);
    font-size: 20px;
    line-height: 1.4;
  }
</style>
</head>
<body>

  <section class="card card--front" aria-label="Business card front">
    <div class="watermark" role="img" aria-label="Faint brand watermark"></div>
    <div class="brand">
      <span class="brand__mark"></span>
      <span class="brand__name">Tarrow Creek<br>Plumbing</span>
    </div>
    <div class="footer-band">
      <span class="website-front">www.yourwebsite.com</span>
    </div>
  </section>

  <section class="card card--back" aria-label="Business card back">
    <div class="watermark" role="img" aria-label="Faint brand watermark"></div>
    <div class="contact-panel"></div>
    <div class="brand">
      <span class="brand__mark"></span>
      <span class="brand__name">Tarrow Creek<br>Plumbing</span>
    </div>

    <div class="person">
      <div class="person__name">YOUR NAME</div>
      <div class="person__title">Your Title</div>
    </div>
    <div class="divider"></div>

    <ul class="contact-list">
      <li>
        <svg viewBox="0 0 24 24" aria-hidden="true"><path d="M6.6 10.8a15.1 15.1 0 0 0 6.6 6.6l2.2-2.2a1 1 0 0 1 1-.25 11.4 11.4 0 0 0 3.6.57 1 1 0 0 1 1 1V20a1 1 0 0 1-1 1A17 17 0 0 1 3 4a1 1 0 0 1 1-1h3.5a1 1 0 0 1 1 1c0 1.25.2 2.45.57 3.57a1 1 0 0 1-.25 1z"/></svg>
        123-456-2100
      </li>
      <li>
        <svg viewBox="0 0 24 24" aria-hidden="true"><path d="M2 5h20v14H2z" fill="none"/><path d="M2 5h20v14H2V5zm2 2v.4l8 5.2 8-5.2V7H4zm16 2.8-8 5.2-8-5.2V17h16V9.8z"/></svg>
        youremail@mailbox.com
      </li>
      <li>
        <svg viewBox="0 0 24 24" aria-hidden="true"><path d="M12 2a10 10 0 1 0 0 20 10 10 0 0 0 0-20zm6.9 6h-3a15.7 15.7 0 0 0-1.3-3.6A8 8 0 0 1 18.9 8zM12 4c.8 1.2 1.5 2.5 1.9 4h-3.8c.4-1.5 1.1-2.8 1.9-4zM4.3 14a8 8 0 0 1 0-4h3.4a16 16 0 0 0 0 4H4.3zm.8 2h3a15.7 15.7 0 0 0 1.3 3.6A8 8 0 0 1 5.1 16zM8 8H5.1a8 8 0 0 1 4.3-3.6C8.8 5.5 8.4 6.7 8 8zm4 12c-.8-1.2-1.5-2.5-1.9-4h3.8c-.4 1.5-1.1 2.8-1.9 4zm2.3-6H9.7a14.7 14.7 0 0 1 0-4h4.6a14.7 14.7 0 0 1 0 4zm.3 5.6c.6-1.1 1-2.3 1.3-3.6h3a8 8 0 0 1-4.3 3.6zm1.7-5.6a16 16 0 0 0 0-4h3.4a8 8 0 0 1 0 4h-3.4z"/></svg>
        www.yourwebsite.com
      </li>
    </ul>

    <address class="address" style="font-style: normal;">
      Your address, city<br>state, ZIP 0000
    </address>
  </section>

</body>
</html>
```